Business Card Design Project

Professional business cards for law firm - a rough example of what we are looking for is attached. The logo, colour and styling of the name are all new and dont need to be changed. We need layout for front and back. We are looking for some imaginative layout of info. We are a young vibrant firm and not too conservative and are not adverse to something quite different.
Updates

Thank you for all the submissions.  We have been blown away with the quality of your work.  Our management team will be meeting later in the week to make our decision.  Again, thanks for the fabulous work.

Industry/Entity Type

Conservative

Requirements
Must have
• Logo and name as in attached example (colour and font)
Should not have
• Scales of Justice

```html
<!DOCTYPE html>
<html lang="en">
<head>
<meta charset="utf-8">
<title>Marlow Reed Legal — Business Cards</title>
<link rel="stylesheet" href="https://fonts.googleapis.com/css2?family=Source+Sans+3:wght@300;400;600;700&display=swap">
<style>
  :root {
    --stage: #e9e7e4;
    --card-top: #ffffff;
    --card-bottom: #e4e4e4;
    --band: #3b3b3d;
    --green: #5b8a2e;
    --ink: #2d2d2f;
    --muted: #6a6a6c;
    --ring: #8d8d8f;
    --on-band: #ffffff;
  }
  * { box-sizing: border-box; margin: 0; padding: 0; }
  html, body { width: 1200px; height: 820px; overflow: hidden; }
  body {
    background: var(--stage);
    font-family: "Source Sans 3", "Helvetica Neue", Arial, sans-serif;
    color: var(--ink);
    display: flex;
    align-items: center;
    justify-content: center;
    gap: 60px;
  }
  .card {
    position: relative;
    width: 540px;
    height: 330px;
    border-radius: 18px;
    overflow: hidden;
    background: linear-gradient(180deg, var(--card-top) 0%, var(--card-bottom) 100%);
    box-shadow: 0 6px 18px rgba(0,0,0,.18);
  }
  .card__band {
    position: absolute;
    left: 0; right: 0; bottom: 0;
    background: var(--band);
  }
  .brand {
    position: absolute;
    display: flex;
    align-items: center;
    gap: 18px;
  }
  .brand__mark {
    flex: none;
    border-radius: 50%;
    border: 3px solid var(--ring);
  }
  .brand__name {
    color: var(--green);
    font-weight: 600;
    line-height: 1;
  }
  .brand__legal {
    display: block;
    color: var(--green);
    font-weight: 600;
    letter-spacing: .32em;
    margin-top: 4px;
  }
  .brand__tagline {
    display: block;
    color: var(--muted);
    font-weight: 400;
    margin-top: 6px;
  }

  /* back: practice areas */
  .card--back .brand { left: 40px; top: 42px; }
  .card--back .brand__mark { width: 110px; height: 110px; }
  .card--back .brand__name { font-size: 38px; }
  .card--back .brand__legal { font-size: 17px; }
  .card--back .brand__tagline { font-size: 15px; }
  .card--back .card__band { height: 62px; }
  .services {
    position: absolute;
    left: 40px; right: 40px; top: 176px;
    display: grid;
    grid-template-columns: 1fr 1fr;
    column-gap: 30px;
    list-style: none;
    font-size: 19px;
    font-weight: 300;
    line-height: 1.08;
    color: var(--ink);
  }
  .services ul { list-style: none; }

  /* front: contact */
  .card--front .brand { left: 40px; top: 34px; }
  .card--front .brand__mark { width: 100px; height: 100px; }
  .card--front .brand__name { font-size: 34px; }
  .card--front .brand__legal { font-size: 15px; }
  .card--front .brand__tagline { font-size: 14px; }
  .person {
    position: absolute;
    left: 40px; top: 160px;
  }
  .person__name { font-size: 26px; font-weight: 700; }
  .person__role { font-size: 17px; font-weight: 400; color: var(--muted); margin-top: 2px; }
  .card--front .card__band {
    height: 88px;
    padding: 0 30px;
    display: flex;
    flex-direction: column;
    justify-content: center;
    gap: 4px;
    color: var(--on-band);
    font-size: 14.5px;
    font-weight: 600;
  }
</style>
</head>
<body>

  <section class="card card--back" aria-label="Card back">
    <div class="brand">
      <span class="brand__mark"></span>
      <div>
        <span class="brand__name">Marlow Reed</span>
        <span class="brand__legal">LEGAL</span>
        <span class="brand__tagline">helping you find the way forward</span>
      </div>
    </div>
    <div class="services">
      <ul>
        <li>Family</li>
        <li>Restraining Orders</li>
        <li>Probate/Wills</li>
        <li>Dividing Fences</li>
      </ul>
      <ul>
        <li>Traffic</li>
        <li>Criminal</li>
        <li>Debt Recovery</li>
        <li>Financial Agreements</li>
      </ul>
    </div>
    <div class="card__band"></div>
  </section>

  <section class="card card--front" aria-label="Card front">
    <div class="brand">
      <span class="brand__mark"></span>
      <div>
        <span class="brand__name">Marlow Reed</span>
        <span class="brand__legal">LEGAL</span>
        <span class="brand__tagline">helping you find the way forward</span>
      </div>
    </div>
    <div class="person">
      <p class="person__name">Clara Dunmore LLB BA</p>
      <p class="person__role">Solicitor</p>
    </div>
    <div class="card__band">
      <p class="contact__address">4/27 Ashgrove Street, Kelmscott WA 6111 PO Box 392, Kelmscott WA 6991</p>
      <p class="contact__lines">T: 9400 1234, 9400 5678 | F: 9400 9012 | E: reception@marlowreedlegal.com.au</p>
    </div>
  </section>

</body>
</html>
```